Website Design for Holbeck Counsel Studio – Clean, Warm, Professional

Maren Holbeck, Esq.
www.MarenTHolbeckLegal.example

I’m a New York City-based attorney and CPA with a reputation for providing thoughtful, high-integrity legal guidance in both estate planning and small business law. I’ve served over 500 clients, and maintain a perfect 5-star rating. Clients come to me for clarity, compassion, and results — and I want my new website to reflect that.

**🎯 WHAT I NEED:**
A clean, modern, and emotionally resonant website that highlights who I am, what I do, and why clients trust me. It must feel approachable and warm, but still professional and elegant — think Quorvex meets boutique law firm. Feminine but not frilly.

**🧩 CORE WEBSITE SECTIONS (Top Navigation):**

1. **Home** – Strong first impression, tagline, CTA (book a call)
Homepage Copy (Sample Layout)
Headline:
Trusted Legal Guidance for Families and Founders.

Subheading:
Whether you’re protecting what you’ve built or building what’s next, I help you navigate estate planning and business law with confidence, compassion, and clarity.

Tagline (beneath logo or footer):
Legal Clarity for Life and Business.
2. **About Maren** – Bio, personal approach, credentials
3. **Services**

* *Estate Planning*
* *Business Law*
4. **Who I Work With** – Ideal clients (parents, entrepreneurs, etc.)
5. **Testimonials** – Client praise and social proof
6. **Success Stories** – Highlighting wins and case types
7. **FAQs** – Warm and clear answers to common questions
8. **Blog** – Thought leadership and helpful tips
8.5 Events
9. **Contact / Book a Call** – Scheduling or contact form

**🖼 STYLE DIRECTION:**

* Clean white backgrounds, soft jewel tones or neutrals
* Professional headshots and personal branding assets available
* Emphasis on readability, trust, and ease of navigation - THIS NEEDS TO BE BUILT OUT SO IT IS TRUSTED BY AI!
* No harsh colors, no corporate/legal clichés (e.g., gavels or scales) - I MEAN THIS. I DO NOT WANT A BORING LAW WEBSITE WITH SCALES AND GAVELS
* Feminine edge (not pink-heavy), with strong hierarchy and callouts

**💡 DESIGN NOTES:**

* Mobile-first design required
* Should include space for video or welcome message
* Easy to update blog or CMS area preferred
* Built in a user-friendly platform like WordPress, Webflow, or similar
* Needs to feel elevated enough to support high-end flat fee packages

**📣 TONE:**
Smart. Warm. Sophisticated. Human.

**⚖️ FINAL DELIVERABLES:**

* Homepage + 5+ interior pages
* Desktop + mobile views
* Style guide (fonts, colors, buttons)
* Bonus if you can help with copy layout/structure (not just visuals)

**📍TARGET AUDIENCE:**

* Busy professionals and families in NYC
* Women and couples who want peace of mind
* Entrepreneurs and creatives needing solid legal support

Here is my current site: www.MarenTHolbeckLegal.example
And here is a second business I have: www.QuickDayCounselDesk.example

Target Market(s)

Families and business owners

Industry/Entity Type

Law

Number of Pages Required

5+ page

Font styles to use
Serif
Sans Serif
Script

Requirements
Must have
• This website must be built to be seen as trustworthy by AI.

```html
<!DOCTYPE html>
<html lang="en">
<head>
<meta charset="utf-8">
<title>Holbeck Counsel Studio — Maren Holbeck, Esq.</title>
<link href="https://fonts.googleapis.com/css2?family=Playfair+Display:wght@400;600;700&family=Open+Sans:wght@400;600;700&display=swap" rel="stylesheet">
<style>
:root{
  --teal:#1a97a6;
  --teal-dark:#137f8c;
  --ink:#1e2a33;
  --text:#3d4850;
  --navy:#2d3b48;
  --slate:#3e4d5a;
  --mist:#e6f3f5;
  --sky:#cbe6ec;
  --white:#ffffff;
  --line:#9fd3da;
  --ghost:#eef1f3;
}
*{box-sizing:border-box;margin:0;padding:0}
html,body{width:1200px;height:4637px;overflow:hidden}
body{position:relative;font-family:"Open Sans",Arial,sans-serif;color:var(--text);background:var(--white)}
h1,h2,h3,h4,h5,h6{font-weight:400}
.serif{font-family:"Playfair Display",Georgia,serif}
.abs{position:absolute}
.btn{position:absolute;display:flex;align-items:center;justify-content:center;background:var(--teal);color:var(--white);font-family:"Playfair Display",Georgia,serif;font-weight:700;font-size:11px}
.btn-outline{position:absolute;display:flex;align-items:center;justify-content:center;background:var(--white);border:1.5px solid var(--teal);color:var(--ink);font-family:"Playfair Display",Georgia,serif;font-weight:700;font-size:11px}
.photo{position:absolute}
.eyebrow{position:absolute;font-size:12px;display:flex;align-items:center;gap:12px}
.eyebrow::after{content:"";width:56px;height:1px;background:var(--teal)}
.center-title{position:absolute;left:0;width:1200px;display:flex;align-items:center;justify-content:center;gap:18px;font-family:"Playfair Display",Georgia,serif}
.center-title::before,.center-title::after{content:"";width:80px;height:1px;background:var(--teal)}
.arrow-circle{position:absolute;width:30px;height:30px;border:1.5px solid var(--teal);border-radius:50%;display:flex;align-items:center;justify-content:center}

/* brand name */
.brand{position:absolute;font-family:"Open Sans",Arial,sans-serif;font-weight:700;font-size:17px;color:var(--white);white-space:nowrap}

/* nav */
.nav{position:absolute;left:0;top:0;width:1200px;height:58px;background:var(--navy)}
.nav .brand{left:120px;top:17px}
.nav-links{position:absolute;left:513px;top:20px;display:flex;gap:24px;font-size:11.5px;color:#dfe6ea}
.nav-links .active{color:var(--teal);text-decoration:underline}

/* hero */
.hero{position:absolute;left:0;top:58px;width:1200px;height:529px;background:linear-gradient(90deg,#eaf6f8 0%,#dff0f3 45%,#cfe4ea 100%)}
.hero h1{position:absolute;left:120px;top:136px;font-family:"Playfair Display",Georgia,serif;font-weight:700;font-size:37px;line-height:50px;color:var(--ink)}
.hero p{position:absolute;left:120px;top:295px;width:450px;font-size:11.5px;line-height:19px}

/* about */
.about-title{position:absolute;left:636px;top:698px;font-family:"Playfair Display",Georgia,serif;font-weight:400;font-size:30px;line-height:38px;color:var(--ink)}
.about-text{position:absolute;left:636px;top:784px;width:420px;font-size:11px;line-height:19px}
.ghost-word{position:absolute;left:0;top:962px;width:1200px;text-align:center;font-family:"Open Sans",Arial,sans-serif;font-weight:700;font-size:80px;line-height:90px;color:var(--ghost);white-space:nowrap}

/* services */
.services{position:absolute;left:0;top:1053px;width:1200px;height:446px;background:linear-gradient(180deg,#48576a,#3a4754 60%,#2f3b46)}
.svc-card{position:absolute;top:1153px;width:470px;height:307px;background:var(--white);border-radius:6px;overflow:hidden}
.svc-label{position:absolute;left:0;bottom:0;width:100%;height:57px;border-left:6px solid var(--teal);display:flex;align-items:center;justify-content:space-between;padding:0 24px;font-family:"Playfair Display",Georgia,serif;font-weight:700;font-size:21px;color:var(--ink)}
.svc-go{width:32px;height:32px;border-radius:50%;background:var(--teal);display:flex;align-items:center;justify-content:center}

/* who */
.who-card{position:absolute;top:1628px;width:225px;height:137px;background:var(--mist);border-radius:14px}
.who-card .ic{position:absolute;left:14px;top:22px;width:48px;height:48px;border-radius:50%;background:var(--white);border:1px solid var(--line);display:flex;align-items:center;justify-content:center}
.who-card h4{position:absolute;left:80px;top:32px;font-family:"Playfair Display",Georgia,serif;font-weight:700;font-size:13px;line-height:16px;color:var(--ink)}
.who-card a{position:absolute;left:80px;font-size:10.5px;color:var(--teal);font-weight:700;text-decoration:underline}
.who-card.on{background:var(--teal)}
.who-card.on h4,.who-card.on a{color:var(--white)}

/* testimonials */
.testi{position:absolute;left:0;top:1826px;width:1200px;height:549px;background:linear-gradient(90deg,#2f3a44,#4a5560 45%,#8a8f8f 80%,#6f6a64)}
.testi-card{position:absolute;left:120px;top:1998px;width:775px;height:313px;background:var(--white);border-radius:6px}
.quote{position:absolute;left:0;top:114px;width:775px;text-align:center;font-size:21px;line-height:28px;color:#2a3238}

/* blog */
.blog-card{position:absolute;background:var(--white);border:1.5px solid var(--line);border-radius:8px}
.blog-card h5{position:absolute;font-family:"Playfair Display",Georgia,serif;font-weight:700;font-size:13px;line-height:17px;color:var(--ink)}
.blog-card p{position:absolute;font-size:9.5px;line-height:12px}

/* success */
.success{position:absolute;left:0;top:2995px;width:1200px;height:558px;background:var(--sky)}
.story-img{position:absolute;top:3163px;width:307px;height:181px;border-radius:6px}
.story-card{position:absolute;top:3289px;width:253px;height:133px;background:var(--white);border-radius:6px;text-align:center}
.story-card h6{margin-top:22px;font-family:"Playfair Display",Georgia,serif;font-weight:700;font-size:13px;line-height:17px;color:var(--ink)}

/* faq */
.faq{position:absolute;left:231px;width:733px;border:1.5px solid var(--line);border-radius:4px;background:var(--white)}
.faq .q{position:absolute;left:19px;top:24px;font-size:13.5px;color:var(--ink)}
.faq .sign{position:absolute;right:22px;top:20px}

/* talk */
.talk{position:absolute;left:0;top:4069px;width:1200px;height:234px;background:linear-gradient(90deg,#2c3843,#3d4852 50%,#2a333b)}

/* footer */
.footer{position:absolute;left:0;top:4303px;width:1200px;height:334px;background:var(--navy);color:#d6dde2}
.footer .brand{left:120px;top:58px}
.footer h6{position:absolute;top:64px;font-family:"Playfair Display",Georgia,serif;font-weight:400;font-size:13px;color:var(--white)}
.flist{position:absolute;top:98px;font-size:9.5px;line-height:23.5px}
.fitem{position:absolute;display:flex;align-items:center;gap:10px;font-size:9px;white-space:nowrap}
.fbox{width:24px;height:24px;border:1px solid var(--teal);border-radius:4px;display:flex;align-items:center;justify-content:center}
</style>
</head>
<body>

<!-- Navigation -->
<header class="nav">
  <div class="brand">Holbeck Counsel Studio</div>
  <nav class="nav-links">
    <span class="active">Home</span><span>About Us</span><span>Services ⌄</span><span>Success Stories</span><span>FAQs</span><span>Blog</span><span>Events</span>
  </nav>
  <div class="btn" style="left:976px;top:10px;width:103px;height:34px;font-family:'Open Sans',sans-serif;font-size:11px">Book a Call</div>
</header>

<!-- Hero -->
<section class="hero">
  <div class="photo" role="img" aria-label="Portrait of the attorney in a robe before a columned courthouse" style="left:560px;top:0;width:640px;height:529px;background:linear-gradient(90deg,rgba(223,240,243,0) 0%,#b9ccd3 35%,#8fa3ad 70%,#aab9c0 100%)"></div>
  <div class="eyebrow" style="left:120px;top:110px;color:var(--teal);font-size:10.5px">Welcome To Holbeck Counsel Studio</div>
  <h1>Trusted Legal<br>Guidance for Families<br>and Founders.</h1>
  <p>Whether you’re protecting what you’ve built or building what’s next, I help you navigate estate planning and business law with confidence, compassion, and clarity.</p>
  <div class="btn" style="left:120px;top:357px;width:197px;height:44px">Book a Free Consultation</div>
</section>

<!-- About -->
<section>
  <div class="photo" role="img" aria-label="Empty courtroom interior" style="left:120px;top:651px;width:310px;height:237px;background:linear-gradient(135deg,#8b8f92,#3c4145)"></div>
  <div class="photo" role="img" aria-label="Attorney seated at her desk" style="left:292px;top:740px;width:288px;height:188px;background:linear-gradient(135deg,#c9bfae,#5e5a55);border:4px solid var(--white);border-radius:6px"></div>
  <div class="abs" style="left:437px;top:651px;width:143px;height:82px;background:var(--teal);border:4px solid var(--white);border-radius:6px;color:var(--white);text-align:center;font-weight:700;padding-top:14px;line-height:22px"><span style="font-size:22px">20</span> <span style="font-size:15px">YEARS</span><br><span style="font-size:15px">EXPERIENCE</span></div>
  <div class="eyebrow" style="left:636px;top:677px;color:var(--text);font-size:10.5px">About Us</div>
  <h2 class="about-title">Hi, I’m Maren — Attorney. CPA.<br>Advocate for your peace of mind.</h2>
  <p class="about-text">With over 500 clients served and a 5-star reputation, I blend legal precision with personal attention. Whether you’re navigating wills and trusts or forming an LLC, I offer legal strategies that are as thoughtful as they are effective.</p>
  <div class="btn" style="left:636px;top:865px;width:109px;height:36px">Learn More</div>
  <div class="ghost-word" aria-hidden="true">Holbeck Counsel Studio</div>
</section>

<!-- Services -->
<section class="services">
  <div class="center-title" style="top:30px;color:var(--white);font-size:30px">Our Services</div>
</section>
<div class="svc-card" style="left:120px">
  <div class="photo" role="img" aria-label="Attorney reviewing documents with a client" style="left:0;top:0;width:470px;height:250px;background:linear-gradient(135deg,#5b6570,#b9aa98 60%,#d8cbb9)"></div>
  <div class="svc-label">Estate Planning
    <span class="svc-go"><svg width="14" height="14" viewBox="0 0 14 14"><path d="M3 11L11 3M5 3h6v6" stroke="#fff" stroke-width="2" fill="none"/></svg></span></div>
</div>
<div class="svc-card" style="left:610px">
  <div class="photo" role="img" aria-label="Hands signing a contract beside a laptop" style="left:0;top:0;width:470px;height:250px;background:linear-gradient(135deg,#e9eaea,#9ea4a8 60%,#6d6a62)"></div>
  <div class="svc-label">Business Law
    <span class="svc-go"><svg width="14" height="14" viewBox="0 0 14 14"><path d="M3 11L11 3M5 3h6v6" stroke="#fff" stroke-width="2" fill="none"/></svg></span></div>
</div>

<!-- Who I Work With -->
<section>
  <div class="center-title" style="top:1548px;color:var(--ink);font-size:29px">Who I Work With</div>
  <div class="arrow-circle" style="left:68px;top:1682px"><svg width="10" height="10" viewBox="0 0 10 10"><path d="M7 1L3 5l4 4" stroke="#1a97a6" stroke-width="1.6" fill="none"/></svg></div>
  <div class="arrow-circle" style="left:1100px;top:1682px"><svg width="10" height="10" viewBox="0 0 10 10"><path d="M3 1l4 4-4 4" stroke="#1a97a6" stroke-width="1.6" fill="none"/></svg></div>
  <div class="who-card" style="left:120px">
    <div class="ic"><svg width="24" height="24" viewBox="0 0 24 24" fill="none" stroke="#1a97a6" stroke-width="1.4"><circle cx="8" cy="8" r="3"/><circle cx="16" cy="8" r="3"/><path d="M3 20c0-4 3-6 5-6s5 2 5 6M11 20c0-4 3-6 5-6s5 2 5 6"/></svg></div>
    <h4>Busy Parents</h4><a style="top:62px">Learn More</a>
  </div>
  <div class="who-card" style="left:365px">
    <div class="ic"><svg width="24" height="24" viewBox="0 0 24 24" fill="none" stroke="#1a97a6" stroke-width="1.4"><circle cx="12" cy="8" r="4"/><path d="M4 21c0-5 4-7 8-7s8 2 8 7"/></svg></div>
    <h4>Entrepreneurs &amp;<br>Small Business<br>Owners</h4><a style="top:96px">Learn More</a>
  </div>
  <div class="who-card on" style="left:610px">
    <div class="ic"><svg width="24" height="24" viewBox="0 0 24 24" fill="none" stroke="#1a97a6" stroke-width="1.4"><circle cx="12" cy="8" r="4"/><path d="M4 21c0-5 4-7 8-7s8 2 8 7"/><rect x="14" y="15" width="6" height="5"/></svg></div>
    <h4>Professionals<br>&amp; Founders</h4><a style="top:79px">Learn More</a>
  </div>
  <div class="who-card" style="left:853px">
    <div class="ic"><svg width="24" height="24" viewBox="0 0 24 24" fill="none" stroke="#1a97a6" stroke-width="1.4"><circle cx="12" cy="12" r="9"/><circle cx="12" cy="10" r="3"/><path d="M7 18c1-3 3-4 5-4s4 1 5 4"/></svg></div>
    <h4>High-Net-Worth<br>Individuals</h4><a style="top:79px">Learn More</a>
  </div>
</section>

<!-- Testimonials -->
<section class="testi">
  <div class="photo" role="img" aria-label="Attorney walking with a clipboard" style="left:900px;top:0;width:240px;height:549px;background:linear-gradient(180deg,#8c8070,#f0ece6 45%,#3a3a3c)"></div>
  <div class="center-title" style="top:56px;color:var(--white);font-size:17px;font-family:'Open Sans',sans-serif">Testimonials</div>
  <div class="abs" style="left:0;top:93px;width:1200px;text-align:center;color:var(--white);font-family:'Playfair Display',Georgia,serif;font-size:28px">Real Clients. Real Results.</div>
  <div class="arrow-circle" style="left:68px;top:313px"><svg width="10" height="10" viewBox="0 0 10 10"><path d="M7 1L3 5l4 4" stroke="#1a97a6" stroke-width="1.6" fill="none"/></svg></div>
</section>
<div class="testi-card">
  <svg class="abs" style="left:440px;top:32px" width="54" height="40" viewBox="0 0 54 40"><path d="M4 40V22C4 10 10 3 22 0l2 5c-7 3-10 8-10 13h10v22zM30 40V22C30 10 36 3 48 0l2 5c-7 3-10 8-10 13h10v22z" fill="#1a97a6"/></svg>
  <p class="quote">“Maren made a complex process feel simple and empowering.<br>We now have peace of mind about our family’s future.”</p>
  <div class="abs" style="left:0;top:184px;width:775px;text-align:center;font-weight:700;font-size:13.5px;color:var(--ink)">Nadia R., Brooklyn</div>
  <div class="abs" role="img" aria-label="Client portrait" style="left:376px;top:223px;width:45px;height:45px;border-radius:50%;background:#4a4e52"></div>
  <div class="abs" role="img" aria-label="Client portrait" style="left:434px;top:214px;width:68px;height:68px;border-radius:50%;background:#2b2f33;border:3px solid #d0d5d8"></div>
  <div class="abs" role="img" aria-label="Client portrait" style="left:515px;top:223px;width:45px;height:45px;border-radius:50%;background:#5a5650"></div>
</div>
<div class="arrow-circle" style="left:1100px;top:2139px;background:rgba(255,255,255,.2)"><svg width="10" height="10" viewBox="0 0 10 10"><path d="M3 1l4 4-4 4" stroke="#1a97a6" stroke-width="1.6" fill="none"/></svg></div>

<!-- Blog -->
<section>
  <div class="eyebrow" style="left:120px;top:2435px;color:var(--ink);font-size:14px">Blog</div>
  <h2 class="abs serif" style="left:120px;top:2463px;font-weight:400;font-size:29px;color:var(--ink)">Legal Tips, Simplified.</h2>
  <div class="btn-outline" style="left:970px;top:2455px;width:108px;height:36px">View All Blog</div>

  <article class="blog-card" style="left:120px;top:2541px;width:468px;height:188px">
    <div class="photo" role="img" aria-label="Attorney holding a small house model" style="left:10px;top:10px;width:160px;height:165px;border-radius:6px;background:linear-gradient(135deg,#a89580,#3a3f45)"></div>
    <h5 style="left:186px;top:26px">5 Things Every Parent Should<br>Include in Their Estate Plan</h5>
    <p style="left:186px;top:68px;width:260px">A must-read checklist for protecting your children and avoiding common missteps.</p>
    <div class="btn-outline" style="left:186px;top:125px;width:110px;height:34px">Learn More</div>
  </article>
  <article class="blog-card" style="left:120px;top:2747px;width:468px;height:188px">
    <div class="photo" role="img" aria-label="Family talking with an aging parent" style="left:10px;top:10px;width:160px;height:165px;border-radius:6px;background:linear-gradient(135deg,#dcd8d0,#6a7178)"></div>
    <h5 style="left:186px;top:22px">How to Talk to Aging Parents<br>About Their Will</h5>
    <p style="left:186px;top:64px;width:260px">Sensitive strategies for starting important conversations without conflict.</p>
    <div class="btn-outline" style="left:186px;top:121px;width:110px;height:34px">Learn More</div>
  </article>
  <article class="blog-card" style="left:604px;top:2541px;width:469px;height:393px">
    <div class="photo" role="img" aria-label="Woman on a phone call outside an office" style="left:12px;top:12px;width:443px;height:225px;border-radius:6px;background:linear-gradient(135deg,#9aa5ad,#4f585e 60%,#7d6c66)"></div>
    <h5 style="left:16px;top:262px">Starting a Business in NYC? Avoid These Legal Mistakes</h5>
    <p style="left:16px;top:284px;width:340px">Learn how to build your business on a solid legal foundation — from day one.</p>
    <div class="btn-outline" style="left:16px;top:336px;width:110px;height:36px">Learn More</div>
  </article>
</section>

<!-- Success Stories -->
<section class="success">
  <div class="center-title" style="top:58px;color:var(--ink);font-size:14px;font-family:'Open Sans',sans-serif">Success Stories</div>
  <div class="abs serif" style="left:0;top:90px;width:1200px;text-align:center;font-size:28px;color:var(--ink)">Legal Wins That Matter</div>
</section>
<div class="arrow-circle" style="left:68px;top:3238px"><svg width="10" height="10" viewBox="0 0 10 10"><path d="M7 1L3 5l4 4" stroke="#1a97a6" stroke-width="1.6" fill="none"/></svg></div>
<div class="arrow-circle" style="left:1100px;top:3238px"><svg width="10" height="10" viewBox="0 0 10 10"><path d="M3 1l4 4-4 4" stroke="#1a97a6" stroke-width="1.6" fill="none"/></svg></div>
<div class="story-img" role="img" aria-label="Family meeting with their attorney" style="left:120px;background:linear-gradient(135deg,#3f5a78,#c7b7a6)"></div>
<div class="story-img" role="img" aria-label="Business partners reviewing papers" style="left:446px;background:linear-gradient(135deg,#d8d2c8,#59616a)"></div>
<div class="story-img" role="img" aria-label="Multi-generation family smiling" style="left:771px;background:linear-gradient(135deg,#c9c7c2,#8a7f78)"></div>
<div class="story-card" style="left:147px"><h6>Family estate saved<br>from probate</h6><div class="btn-outline" style="left:71px;top:75px;width:110px;height:34px;font-family:'Open Sans',sans-serif;font-weight:400">Read More</div></div>
<div class="story-card" style="left:473px"><h6>LLC formation with tax<br>strategy baked in</h6><div class="btn-outline" style="left:71px;top:75px;width:110px;height:34px;font-family:'Open Sans',sans-serif;font-weight:400">Read More</div></div>
<div class="story-card" style="left:798px"><h6>Family estate saved<br>from probate</h6><div class="btn-outline" style="left:71px;top:75px;width:110px;height:34px;font-family:'Open Sans',sans-serif;font-weight:400">Read More</div></div>
<div class="btn" style="left:530px;top:3455px;width:140px;height:36px">Read More Stories</div>

<!-- FAQ -->
<section>
  <div class="abs serif" style="left:0;top:3600px;width:1200px;text-align:center;font-size:29px;color:var(--ink)">Got Questions?</div>
  <div class="faq" style="top:3678px;height:70px"><span class="q">What’s included in an estate plan?</span>
    <svg class="sign" width="24" height="24" viewBox="0 0 24 24"><path d="M12 2v20M2 12h20" stroke="#1a97a6" stroke-width="2.4"/></svg></div>
  <div class="faq" style="top:3763px;height:92px"><span class="q">Can I update my will later?</span>
    <span class="abs" style="left:19px;top:52px;font-size:11px">Absolutely. Your estate plan should evolve as your life does — and I make updates simple and stress-free.</span>
    <svg class="sign" width="24" height="24" viewBox="0 0 24 24"><path d="M4 12h16" stroke="#1a97a6" stroke-width="2.4"/></svg></div>
  <div class="faq" style="top:3872px;height:68px"><span class="q">Do I need a lawyer to form an LLC?</span>
    <svg class="sign" width="24" height="24" viewBox="0 0 24 24"><path d="M12 2v20M2 12h20" stroke="#1a97a6" stroke-width="2.4"/></svg></div>
  <div class="btn" style="left:546px;top:3970px;width:108px;height:36px">See All FAQs</div>
</section>

<!-- Call to action -->
<section class="talk">
  <div class="photo" role="img" aria-label="Dim library shelves with a desk in the foreground" style="left:600px;top:0;width:600px;height:234px;background:linear-gradient(90deg,rgba(61,72,82,0),#4b4740 60%,#2a2622)"></div>
  <div class="center-title" style="top:50px;color:var(--white);font-size:30px">Let’s Talk.</div>
  <div class="abs" style="left:0;top:100px;width:1200px;text-align:center;color:var(--white);font-size:11px">Ready to get started? Schedule your free discovery call today.</div>
  <div class="btn" style="left:530px;top:138px;width:140px;height:36px">Read More Stories</div>
</section>

<!-- Footer -->
<footer class="footer">
  <div class="brand">Holbeck Counsel Studio</div>
  <p class="abs" style="left:120px;top:96px;width:200px;font-size:9px;line-height:17.5px">I’m a New York City-based attorney and CPA with a reputation for providing thoughtful, high-integrity legal guidance in both estate planning and small business law. I’ve served over 500 clients, and maintain a perfect 5-star rating.</p>

  <h6 style="left:396px">Quick Links</h6>
  <div class="flist" style="left:396px">Home<br>About Us<br>Services<br>Success Stories<br>FAQs<br>Blog<br>Events</div>

  <h6 style="left:548px">Contact Info</h6>
  <div class="fitem" style="left:548px;top:100px"><span class="fbox"><svg width="12" height="12" viewBox="0 0 12 12"><path d="M2 1l2 0 1 3-1.5 1a7 7 0 0 0 3.5 3.5L8 7l3 1v2c0 .6-.4 1-1 1A9 9 0 0 1 1 2c0-.6.4-1 1-1z" fill="none" stroke="#1a97a6"/></svg></span>+1 212 555 0148</div>
  <div class="fitem" style="left:548px;top:135px;color:var(--teal)"><span class="fbox"><svg width="12" height="10" viewBox="0 0 12 10"><rect x="0.5" y="0.5" width="11" height="9" fill="none" stroke="#1a97a6"/><path d="M1 1l5 4 5-4" fill="none" stroke="#1a97a6"/></svg></span>hello@holbeckcounsel.example</div>
  <div class="fitem" style="left:548px;top:170px"><span class="fbox"><svg width="12" height="12" viewBox="0 0 12 12"><circle cx="6" cy="6" r="5" fill="none" stroke="#1a97a6"/><path d="M1 6h10M6 1c3 3 3 7 0 10M6 1c-3 3-3 7 0 10" fill="none" stroke="#1a97a6"/></svg></span>holbeckcounsel.example</div>

  <h6 style="left:748px">Follow Us</h6>
  <div class="fitem" style="left:748px;top:100px"><span class="fbox"><svg width="8" height="8"><circle cx="4" cy="4" r="3.5" fill="#1a97a6"/></svg></span>Linkfold</div>
  <div class="fitem" style="left:748px;top:135px"><span class="fbox"><svg width="8" height="8"><circle cx="4" cy="4" r="3.5" fill="#1a97a6"/></svg></span>Picturo</div>
  <div class="fitem" style="left:748px;top:170px"><span class="fbox"><svg width="8" height="8"><circle cx="4" cy="4" r="3.5" fill="#1a97a6"/></svg></span>Chirpline</div>

  <h6 style="left:882px">Newsletter Signup</h6>
  <div class="abs" style="left:882px;top:96px;width:196px;height:36px;border:1px solid #56656f;font-size:9px;padding:12px 14px">Email</div>
  <div class="btn" style="left:882px;top:139px;width:196px;height:36px;font-size:11px">Subscribe</div>

  <div class="abs" style="left:120px;top:272px;width:958px;height:1px;background:#4b5a66"></div>
  <div class="abs" style="left:120px;top:284px;font-size:9px">© 2025 Holbeck Counsel Studio All rights reserved.</div>
  <div class="abs" style="left:826px;top:284px;font-size:9px;display:flex;gap:14px"><span>Company</span><span>Privacy Policy</span><span>Terms and Conditions</span></div>
</footer>

</body>
</html>
```